Torvel, Inc. new buisness cards - brand guide included

We need new business cards. SLEAK SIMPLE FINANCE. They must include a place for NAME, TITLE, CELL, OFFICE PHONE, EMAIL. they also must include our services across the bottom. AIR, OCEAN, FTL, LTL, EXPRESS. for reference this will be being handed to some of the most prestigious shipping companies in a america.

Target Market(s)

Finance and corporate

Contact Information for Business Card

We need new business cards. SLEAK SIMPLE FINANCE. They must include a place for NAME, TITLE, CELL, OFFICE PHONE, EMAIL. they also must include our services across the bottom. AIR, OCEAN, FTL, LTL, EXPRESS.

Requirements
Must have
• We need new business cards. SLEAK SIMPLE FINANCE. They must include a place for NAME, TITLE, CELL, OFFICE PHONE, EMAIL. they also must include our services across the bottom. AIR, OCEAN, FTL, LTL, EXPRESS.
Nice to have
• USE THE COLORS AND LOGO IN THE BRAND GUIDE :)

```html
<!DOCTYPE html>
<html lang="en">
<head>
<meta charset="utf-8">
<title>Torvel, Inc. Business Card</title>
<link rel="stylesheet" href="https://fonts.googleapis.com/css2?family=Tinos:wght@400;700&display=swap">
<style>
  :root {
    --bg: #3a3a3a;
    --card-dark: #1f1f1f;
    --gold: #c9b99a;
    --card-light: #ffffff;
    --ink: #262626;
  }
  * { margin: 0; padding: 0; box-sizing: border-box; }
  html, body { width: 1200px; height: 758px; overflow: hidden; }
  body {
    background: var(--bg);
    font-family: "Tinos", "Times New Roman", serif;
    position: relative;
  }
  .card {
    position: absolute;
    top: 224px;
    width: 540px;
    height: 309px;
    border-radius: 18px;
  }
  .card--front { left: 40px; background: var(--card-dark); color: var(--gold); }
  .card--back { left: 620px; background: var(--card-light); color: var(--ink); }

  .front-name {
    position: absolute;
    left: 0; right: 0; top: 96px;
    text-align: center;
    font-size: 74px;
    letter-spacing: 4px;
    line-height: 1;
  }
  .services {
    position: absolute;
    left: 0; right: 0; top: 206px;
    text-align: center;
    font-size: 15px;
    letter-spacing: 1px;
  }
  .services span::before { content: "\2022"; margin: 0 6px 0 10px; }
  .services span:first-child::before { margin-left: 0; }

  .back-name {
    position: absolute;
    left: 28px; top: 118px;
    width: 220px;
    text-align: center;
    font-size: 46px;
    letter-spacing: 3px;
    line-height: 1;
  }
  .divider {
    position: absolute;
    left: 270px; top: 60px;
    width: 1px; height: 150px;
    background: var(--ink);
  }
  .contact {
    position: absolute;
    left: 292px; top: 58px;
  }
  .contact__name { font-size: 19px; font-weight: 700; letter-spacing: 1px; }
  .contact__title { font-size: 15px; margin: 2px 0 10px; }
  .contact__row {
    display: flex; align-items: center; gap: 8px;
    font-size: 15px; line-height: 23px;
  }
  .contact__row svg { width: 14px; height: 14px; flex: none; fill: var(--ink); }
  .address {
    position: absolute;
    left: 0; right: 0; bottom: 34px;
    display: flex; justify-content: center; align-items: center; gap: 8px;
    font-size: 16px;
  }
  .address svg { width: 12px; height: 16px; fill: var(--ink); }
</style>
</head>
<body>
  <section class="card card--front">
    <div class="front-name">TORVEL</div>
    <div class="services"><span>AIR</span><span>OCEAN</span><span>FTL</span><span>LTL</span><span>EXPRESS</span></div>
  </section>

  <section class="card card--back">
    <div class="back-name">TORVEL</div>
    <div class="divider"></div>
    <div class="contact">
      <div class="contact__name">DANIEL WHITCOMBE</div>
      <div class="contact__title">Founder &amp; CEO</div>
      <div class="contact__row">
        <svg viewBox="0 0 16 16"><path d="M2 5c0-2 2-3 6-3s6 1 6 3v1h-3V5H5v1H2z M4 7h8l2 6H2z"/></svg>
        555-018-2740
      </div>
      <div class="contact__row">
        <svg viewBox="0 0 16 16"><path d="M5 1h6a1 1 0 0 1 1 1v12a1 1 0 0 1-1 1H5a1 1 0 0 1-1-1V2a1 1 0 0 1 1-1zm0 2v9h6V3z"/></svg>
        555-018-2740
      </div>
      <div class="contact__row">
        <svg viewBox="0 0 16 16"><path d="M1 3h14v10H1zm1 1v1l6 4 6-4V4z"/></svg>
        accounting@torvelinc.com
      </div>
      <div class="contact__row">
        <svg viewBox="0 0 16 16"><circle cx="8" cy="8" r="7"/></svg>
        www.torvelinc.com
      </div>
    </div>
    <div class="address">
      <svg viewBox="0 0 12 16"><path d="M6 0a6 6 0 0 1 6 6c0 4-6 10-6 10S0 10 0 6a6 6 0 0 1 6-6zm0 3.5A2.5 2.5 0 1 0 6 8.5 2.5 2.5 0 0 0 6 3.5z"/></svg>
      4120 Harlow Creek RD, Dunmore, DE 19904
    </div>
  </section>
</body>
</html>
```